Email Preference Page Design

We are looking for a 2 page design for our users to edit their email preferences and submit friend referrals. You can find the fuctionality, content and text here:

https://brightreel.mailvector.example/app/linkClick/7281/5b9c1d04e6a7f318/20583147/8d4f2a61c0b9e357

* the shipping and billing address might be different so you need to show the billing if the "same as shipping" box is not checked. It can auto-hide like the page above shows if that fits your design.

* when the "unsubscribe from all email lists" box is selected, all the other checkbox options will hide as in the example page. We need you to show us what the site will look like with and without that checkbox selected.

We want to match these two pages to the general feel of these website pages:

www.brightreel.example
and
free.brightreel.example

The page should be very clean and tight. Project is for design only but must be able to be implemented in html showing button and checkbox states. Technically this must be two pages for our system - one for all the user info and one for individual email referrals (see example above).

Target Market(s)

video professionals

Industry/Entity Type

Shipping

Requirements
Must have
• our logo (see numerous versions attached)
well designed header
well designed sections
clean editable text
tight layout
html friendly
easy to understand
2 pages
Nice to have
• custom checkboxes and radio buttons

```html
<!DOCTYPE html>
<html lang="en">
<head>
<meta charset="utf-8">
<title>BrightReel – Communication Preferences</title>
<link href="https://fonts.googleapis.com/css2?family=Courgette&family=Dancing+Script:wght@500&family=Indie+Flower&family=Didact+Gothic&family=Open+Sans:wght@400;600;700&display=swap" rel="stylesheet">
<style>
  :root{
    --page:#f3f2ee;
    --frame:#0e0e0e;
    --panel:#f3e4c2;
    --tag-top:#f2b840;
    --tag-bottom:#dc9a1c;
    --field:#8b8a86;
    --ink:#333;
    --ink-soft:#444;
    --rule:#d9a53a;
    --check:#9a9a96;
    --green:#8fd14f;
    --footer:#1e2a38;
    --footer-ink:#d6dbe2;
  }
  *{box-sizing:border-box;margin:0;padding:0}
  html,body{width:823px;height:1200px;overflow:hidden}
  body{position:relative;background:var(--page);font-family:"Open Sans",sans-serif;color:var(--ink)}
  .abs{position:absolute}

  /* header */
  .masthead{left:0;top:0;width:823px;height:260px;background:var(--frame)}
  .hero-photo{left:48px;top:0;width:727px;height:260px;
    background:radial-gradient(ellipse at 45% 55%,#f3c27a 0%,#c9703a 30%,transparent 60%),
               linear-gradient(100deg,#2a3a58 0%,#8a4a2e 35%,#d88a3c 55%,#3a5a7a 80%,#1c2638 100%)}
  .main-nav{left:48px;top:0;width:727px;height:27px;background:rgba(20,28,40,.82)}
  .main-nav a{position:absolute;top:7px;font-size:10px;font-weight:600;color:#fff;text-decoration:none;white-space:nowrap}
  .main-nav a.current{color:var(--green)}
  .brand{left:184px;top:0;width:88px;height:53px;background:#fff;border-radius:0 0 6px 6px;
    display:flex;align-items:center;justify-content:center;gap:5px}
  .brand-mark{width:9px;height:9px;background:var(--tag-bottom)}
  .brand-name{font-size:13px;font-weight:700;line-height:12px;color:#3a3a3a}
  .hero-title{left:160px;top:90px;width:360px;text-align:center;font-family:"Courgette",cursive;font-size:20px;line-height:27px;color:#fff;white-space:nowrap;text-shadow:0 1px 3px rgba(0,0,0,.5)}
  .hero-sub{left:175px;top:156px;font-size:11px;color:#fff;text-shadow:0 1px 2px rgba(0,0,0,.6)}

  /* banner tags */
  .tag{display:flex;align-items:center;justify-content:center;color:#fff;white-space:nowrap;padding:0 14px;
    background:linear-gradient(var(--tag-top),var(--tag-bottom));
    clip-path:polygon(10px 0,calc(100% - 10px) 0,100% 50%,calc(100% - 10px) 100%,10px 100%,0 50%)}
  .tag.hand{font-family:"Dancing Script",cursive;font-weight:500;font-size:12px;color:#4a3410}
  .tag.hand.wide{font-size:14px}
  .rule{height:1px;background:var(--rule)}
  .rule.soft{background:#d8d4c8}

  .section-title{font-family:"Indie Flower",cursive;font-size:20px;color:#222}
  .panel{background:var(--panel)}
  .field{height:18px;background:var(--field);border:1px solid #777}

  .check{width:16px;height:16px;background:var(--check);border-radius:2px}
  .check::after{content:"";position:absolute;left:5px;top:1px;width:5px;height:10px;border:solid #fff;border-width:0 2px 2px 0;transform:rotate(40deg)}
  .check.sm{width:13px;height:13px}
  .check.sm::after{left:4px;top:1px;width:4px;height:8px}

  .note{font-family:"Indie Flower",cursive;font-size:13.5px;color:#333;white-space:nowrap}
  .filter-head{left:0;top:743px;width:823px;text-align:center;font-family:"Didact Gothic",sans-serif;font-size:16px;color:#222}
  .option-list{list-style:none}
  .option-list li{position:relative;height:14.5px;padding-left:24px;font-family:"Didact Gothic",sans-serif;font-size:11.5px;line-height:14px;color:var(--ink-soft);white-space:nowrap}
  .option-list li .check{position:absolute;left:0;top:1px}

  .submit{left:288px;top:1042px;width:242px;height:25px;font-family:"Didact Gothic",sans-serif;font-size:15px;color:#222}

  .site-footer{left:0;top:1125px;width:823px;height:75px;background:var(--footer);text-align:center;color:var(--footer-ink)}
  .footer-links{margin-top:19px;font-size:6.5px}
  .footer-links a{color:var(--footer-ink);text-decoration:none;margin:0 3px}
  .copyright{margin-top:3px;font-size:6px}
  .social{margin-top:5px;display:flex;justify-content:center;gap:3px}
  .social span{width:13px;height:13px;border-radius:50%;border:1px solid #8a7a4a;background:#2a3444}
</style>
</head>
<body>

<header class="abs masthead">
  <div class="abs hero-photo" role="img" aria-label="Blurred night city street with a taxi and streaking neon lights"></div>
  <nav class="abs main-nav">
    <a style="left:256px" href="#">Free Videos</a>
    <a style="left:324px" href="#">BrightReel</a>
    <a style="left:396px" href="#">Launch Clip</a>
    <a class="current" style="left:470px" href="#">Free Sign-Up</a>
    <a style="left:543px" href="#">About Us</a>
  </nav>
  <div class="abs brand"><span class="brand-mark"></span><span class="brand-name">bright<br>reel</span></div>
  <h1 class="abs hero-title">Free authentic motion loops updated<br>every month for our email subscribers</h1>
  <p class="abs hero-sub">Simply sign-up and we will send you this month's password.</p>
</header>

<main>
  <div class="abs rule soft" style="left:47px;top:281px;width:726px"></div>
  <div class="abs tag" style="left:292px;top:271px;width:240px;height:21px;font-size:10px">Communication Preferences</div>

  <h2 class="abs section-title" style="left:53px;top:326px">Contact Info -</h2>
  <section class="abs panel" style="left:45px;top:368px;width:695px;height:150px"></section>
  <div class="abs rule" style="left:63px;top:397px;width:420px;opacity:.4"></div>
  <div class="abs rule" style="left:63px;top:432px;width:420px;opacity:.4"></div>
  <div class="abs rule" style="left:63px;top:466px;width:645px;opacity:.4"></div>
  <div class="abs rule" style="left:63px;top:500px;width:645px;opacity:.4"></div>

  <div class="abs tag hand" style="left:63px;top:380px;width:74px;height:17px">First Name *</div>
  <div class="abs field" style="left:149px;top:380px;width:111px"></div>
  <div class="abs tag hand" style="left:288px;top:380px;width:75px;height:17px">Last Name *</div>
  <div class="abs field" style="left:375px;top:380px;width:110px"></div>

  <div class="abs tag hand" style="left:63px;top:415px;width:74px;height:17px">Email *</div>
  <div class="abs field" style="left:147px;top:415px;width:111px"></div>
  <div class="abs tag hand" style="left:288px;top:415px;width:75px;height:17px">Phone</div>
  <div class="abs field" style="left:372px;top:415px;width:110px"></div>

  <div class="abs tag hand" style="left:63px;top:449px;width:74px;height:17px">Adress 1</div>
  <div class="abs field" style="left:149px;top:449px;width:111px"></div>
  <div class="abs tag hand" style="left:288px;top:449px;width:75px;height:17px">Adress 2</div>
  <div class="abs field" style="left:375px;top:449px;width:110px"></div>
  <div class="abs tag hand" style="left:514px;top:449px;width:74px;height:17px">Adress 3</div>
  <div class="abs field" style="left:599px;top:449px;width:111px"></div>

  <div class="abs tag hand" style="left:63px;top:483px;width:74px;height:17px">City</div>
  <div class="abs field" style="left:149px;top:483px;width:111px"></div>
  <div class="abs tag hand" style="left:288px;top:483px;width:75px;height:17px">Country</div>
  <div class="abs field" style="left:375px;top:483px;width:110px"></div>
  <div class="abs tag hand" style="left:514px;top:483px;width:74px;height:17px">State</div>
  <div class="abs field" style="left:601px;top:483px;width:111px"></div>

  <h2 class="abs section-title" style="left:52px;top:551px">Shipping Address -</h2>
  <section class="abs panel" style="left:45px;top:592px;width:695px;height:60px"></section>
  <div class="abs tag hand wide" style="left:63px;top:611px;width:250px;height:23px">Billing address is same as shipping address</div>
  <div class="abs check" style="left:344px;top:615px"></div>

  <div class="abs check" style="left:109px;top:677px"></div>
  <p class="abs note" style="left:139px;top:677px">Subscribe me to your general email list. This monthly email includes free video loops and VIP sale notices</p>
  <div class="abs rule" style="left:32px;top:699px;width:755px"></div>

  <p class="abs filter-head">Help Us Filter Our Emails so we are sending only relevant information to you -</p>

  <section class="abs panel" style="left:45px;top:776px;width:695px;height:240px"></section>
  <div class="abs tag hand wide" style="left:96px;top:804px;width:247px;height:23px">Send me emails about these product types:</div>
  <div class="abs tag hand wide" style="left:439px;top:804px;width:247px;height:23px">I am Involved in or have interest in:</div>

  <ul class="abs option-list" style="left:114px;top:849px">
    <li><span class="check sm"></span>Low energy motion loops</li>
    <li><span class="check sm"></span>High energy motion loops</li>
    <li><span class="check sm"></span>Timelapse footage</li>
    <li><span class="check sm"></span>Worship or wedding motion loops</li>
    <li><span class="check sm"></span>Pre-mixed DVDs and BluRay</li>
    <li><span class="check sm"></span>Entertainment lasers for concerts and clubs</li>
    <li><span class="check sm"></span>Entertainment lasers for text &amp; logo display</li>
    <li><span class="check sm"></span>Custom logo animation services</li>
    <li><span class="check sm"></span>Video software for creating video animations</li>
    <li><span class="check sm"></span>Video software for live performance (Vjing)</li>
  </ul>
  <ul class="abs option-list" style="left:462px;top:849px">
    <li><span class="check sm"></span>VJing (live performance video)</li>
    <li><span class="check sm"></span>DJing (live performance audio+video)</li>
    <li><span class="check sm"></span>Performing in a band</li>
    <li><span class="check sm"></span>Video editing</li>
    <li><span class="check sm"></span>Corporate presentations</li>
    <li><span class="check sm"></span>Worship video services</li>
    <li><span class="check sm"></span>Lasers for entertainment &amp; branding</li>
    <li><span class="check sm"></span>Special offers from BrightReel partners</li>
    <li><span class="check sm"></span>Unsubscribe from all email lists</li>
  </ul>

  <div class="abs rule" style="left:45px;top:1054px;width:727px;background:#c9b27a"></div>
  <div class="abs tag submit">SUBMIT</div>
</main>

<footer class="abs site-footer">
  <p class="footer-links"><a href="#">Free Videos</a><a href="#">BrightReel</a><a href="#">Launch Clip</a><a href="#">Free Sign-Up</a><a href="#">About Us</a><a href="#">Contact Us</a></p>
  <p class="copyright">All Rights Reserved Copyright© 2013 - BrightReel</p>
  <div class="social"><span></span><span></span><span></span></div>
</footer>

</body>
</html>
```